Velmuts release concert (part 2)

Velmuts is a Reggae/Ska band from Oslo , we are releasing our first album called “overgrown” , friday 29th august at a pub called Tarnwells http://www.tarnwells.no
door open starts 21:00
Concert: 22:00
Price : 150kr

i need this to be printed in a3

Great work , could you guys insert the address and phone of the venue : Tarnwells Nedre Kvistveien 4 0462 Oslo Tlf. 937 82 214 Thanks !

```html
<!DOCTYPE html>
<html lang="en">
<head>
<meta charset="utf-8">
<title>Velmuts – overgrown release concert</title>
<link rel="stylesheet" href="https://fonts.googleapis.com/css2?family=Playfair+Display:wght@700;800&family=Arvo:wght@700&family=Kaushan+Script&display=swap">
<style>
  :root {
    --sun: #f7d21e;
    --flame: #ef7d1a;
    --forest: #2f8f3a;
    --leaf: #7cc24a;
    --sky: #29c6e6;
    --wing: #b88ad0;
    --earth: #8a4a1c;
    --rock: #b9b9bd;
    --photo-light: #e6e6e6;
    --photo-mid: #8a8a8a;
    --photo-dark: #2a2a2a;
    --ink: #ffffff;
  }
  * { margin: 0; padding: 0; box-sizing: border-box; }
  html, body { width: 848px; height: 1200px; overflow: hidden; background: #ffffff; }
  .poster {
    position: relative;
    width: 848px;
    height: 1200px;
    overflow: hidden;
    background: var(--photo-dark);
  }
  .illustration {
    position: absolute;
    left: 0; top: 0;
    width: 848px; height: 720px;
    background:
      radial-gradient(ellipse 220px 260px at 424px 390px, rgba(255,120,40,0.55), transparent 70%),
      radial-gradient(ellipse 260px 200px at 424px 260px, rgba(184,138,208,0.85), transparent 75%),
      radial-gradient(ellipse 160px 90px at 424px 650px, rgba(230,240,255,0.9), transparent 80%),
      linear-gradient(180deg,
        var(--sun) 0px,
        var(--flame) 45px,
        var(--forest) 110px,
        var(--leaf) 180px,
        var(--rock) 300px,
        var(--wing) 380px,
        var(--earth) 500px,
        var(--sky) 640px,
        #dfe8ec 720px);
  }
  .band-photo {
    position: absolute;
    left: 0; top: 700px;
    width: 848px; height: 500px;
    background: linear-gradient(180deg, var(--photo-light) 0%, #bdbdbd 30%, var(--photo-mid) 60%, var(--photo-dark) 100%);
  }
  .band-name {
    position: absolute;
    left: 0; top: 62px;
    width: 848px;
    text-align: center;
    font-family: "Kaushan Script", cursive;
    font-size: 50px;
    line-height: 60px;
    color: var(--ink);
  }
  .details {
    position: absolute;
    left: 113px; top: 938px;
    font-family: "Arvo", serif;
    font-weight: 700;
    font-size: 23px;
    line-height: 33px;
    color: var(--ink);
    transform: scaleX(0.86);
    transform-origin: left top;
    white-space: nowrap;
  }
  .album-title {
    position: absolute;
    left: 288px; top: 998px;
    font-family: "Playfair Display", serif;
    font-weight: 800;
    font-size: 112px;
    line-height: 110px;
    letter-spacing: -1px;
    color: var(--ink);
    transform: scaleX(0.88);
    transform-origin: left top;
    white-space: nowrap;
  }
  .date {
    position: absolute;
    left: 26px; top: 1106px;
    font-family: "Playfair Display", serif;
    font-weight: 700;
    font-size: 64px;
    line-height: 70px;
    color: var(--ink);
    transform: scaleX(0.78);
    transform-origin: left top;
    white-space: nowrap;
  }
  .venue {
    position: absolute;
    left: 471px; top: 1126px;
    font-family: "Playfair Display", serif;
    font-weight: 700;
    color: var(--ink);
    white-space: nowrap;
  }
  .venue-name { font-size: 30px; line-height: 38px; transform: scaleX(0.85); transform-origin: left top; }
  .venue-address { font-size: 14px; line-height: 20px; transform: scaleX(0.88); transform-origin: left top; }
</style>
</head>
<body>
  <main class="poster">
    <div class="illustration" role="img" aria-label="Psychedelic illustration of a winged figure meditating among trees, hills, sun, star and moon, with a drum, a scroll, sunflowers and a large eye below"></div>
    <div class="band-photo" role="img" aria-label="Black and white photograph of the seven band members standing on outdoor stairs"></div>

    <h1 class="band-name">Velmuts</h1>

    <div class="details">
      <p>door open starts 21:00</p>
      <p>Concert: 22:00</p>
      <p>Price : 150kr</p>
    </div>

    <h2 class="album-title">overgrown</h2>

    <p class="date">friday 29th august</p>

    <div class="venue">
      <p class="venue-name">at Tarnwells</p>
      <p class="venue-address">Tarnwells Nedre Kvistveien 4 0462 Oslo Tlf. 937 82 214</p>
    </div>
  </main>
</body>
</html>
```